Brennick Framing Company - Card Design

I am looking to use the logo designs that you already did for me to develop a business card. I would like the card to have a black background and be double sided. I want white and green logo and text. I have attached an inspiration photo of a look that I like. I would like to use the Vertical Logo attached to take up the full front side of the card. On the back where I have my name and information, I would like to have the horizontal logo or maybe even just the image of the 'A' and trees without the text. I am open, but I am looking for something clean and simple and I want the green to really pop! Additional files can be found under Design #: 64093528

Target Market(s)

Homeowners

Industry/Entity Type

Construction

Contact Information for Business Card

Name: Marcus Brennick, Title: Project Manager, Phone: 647.382.9105, Email: brennickframingcompany@quillpost.example, address: 418 Larkspur Ln, Felton, CA 95018, Lic# 5836214

Colors
00AB8E
00BBA5
67D7C9
C6EFE9
E9F9F6

Requirements
Nice to have
• I would like to see the logos that I have already got from ArtSwarm, though I am open to new ones

```html
<!DOCTYPE html>
<html lang="en">
<head>
<meta charset="UTF-8">
<title>Brennick Framing Company – Business Card</title>
<link href="https://fonts.googleapis.com/css2?family=Montserrat:wght@400;500;600;700&display=swap" rel="stylesheet">
<style>
  :root {
    --stage: #e4e1dc;
    --card: #232323;
    --green: #5fb546;
    --white: #ffffff;
    --muted: #e6e6e6;
  }
  * { box-sizing: border-box; margin: 0; padding: 0; }
  html, body { width: 900px; height: 1200px; overflow: hidden; }
  body {
    background: var(--stage);
    font-family: "Montserrat", Arial, sans-serif;
    position: relative;
  }
  .card {
    position: absolute;
    left: 82px;
    width: 740px;
    height: 438px;
    background: var(--card);
    border-radius: 24px;
    overflow: hidden;
    box-shadow: -3px 4px 0 var(--green), 0 12px 24px rgba(0,0,0,0.25);
  }
  .card--front { top: 130px; }
  .card--back { top: 638px; }

  /* front */
  .brand-stack {
    position: absolute;
    left: 40px;
    top: 150px;
    width: 305px;
    text-align: center;
    color: var(--white);
    font-weight: 700;
    font-size: 28px;
    line-height: 1.15;
    letter-spacing: 1px;
    text-transform: uppercase;
  }
  .brand-stack .mark {
    display: block;
    width: 34px; height: 34px;
    margin: 0 auto 12px;
    background: var(--green);
  }
  .divider {
    position: absolute;
    left: 343px;
    top: 140px;
    width: 2px;
    height: 204px;
    background: var(--green);
  }
  .details {
    position: absolute;
    left: 378px;
    right: 18px;
    top: 142px;
    color: var(--white);
  }
  .person-name {
    color: var(--green);
    font-size: 27px;
    font-weight: 700;
    line-height: 1.1;
  }
  .person-title {
    font-size: 16px;
    font-weight: 400;
    color: var(--muted);
    margin-top: 4px;
  }
  .licence {
    margin-top: 22px;
    font-size: 16px;
    font-weight: 600;
  }
  .licence span { color: var(--green); }
  .contact-list { list-style: none; margin-top: 18px; }
  .contact-list li {
    display: flex;
    align-items: center;
    gap: 12px;
    font-size: 16px;
    color: var(--muted);
    height: 26px;
    white-space: nowrap;
  }
  .contact-list li.contact-email { font-size: 13px; }
  .contact-list svg { width: 16px; height: 16px; flex: none; fill: var(--green); }

  /* back */
  .brand-line {
    position: absolute;
    left: 0; right: 0;
    top: 192px;
    display: flex;
    justify-content: center;
    align-items: center;
    gap: 18px;
    color: var(--white);
    font-weight: 700;
    font-size: 33px;
    letter-spacing: 1px;
    text-transform: uppercase;
  }
  .brand-line .mark { width: 44px; height: 44px; background: var(--green); }
</style>
</head>
<body>

  <section class="card card--front" aria-label="Card front">
    <div class="brand-stack">
      <span class="mark"></span>
      Brennick<br>Framing<br>Company
    </div>
    <div class="divider"></div>
    <div class="details">
      <h1 class="person-name">Marcus Brennick</h1>
      <p class="person-title">Project Manager</p>
      <p class="licence"><span>Lic</span> #5836214</p>
      <ul class="contact-list">
        <li>
          <svg viewBox="0 0 16 16" aria-hidden="true"><path d="M8 0C4.7 0 2.5 2.4 2.5 5.4 2.5 9.3 8 16 8 16s5.5-6.7 5.5-10.6C13.5 2.4 11.3 0 8 0zm0 7.6a2.2 2.2 0 1 1 0-4.4 2.2 2.2 0 0 1 0 4.4z"/></svg>
          418 Larkspur Ln, Felton, CA 95018
        </li>
        <li>
          <svg viewBox="0 0 16 16" aria-hidden="true"><path d="M2 5c0-1.5 2.7-3 6-3s6 1.5 6 3v1.5h-3V5H5v1.5H2zM3 8h10l1 6H2zm5 1.3a1.8 1.8 0 1 0 0 3.6 1.8 1.8 0 0 0 0-3.6z"/></svg>
          647.382.9105
        </li>
        <li class="contact-email">
          <svg viewBox="0 0 16 16" aria-hidden="true"><path d="M1 3h14v1.2L8 9 1 4.2zm0 2.6 7 4.8 7-4.8V13H1z"/></svg>
          brennickframingcompany@quillpost.example
        </li>
      </ul>
    </div>
  </section>

  <section class="card card--back" aria-label="Card back">
    <div class="brand-line">
      <span class="mark"></span>
      Brennick Framing Company
    </div>
  </section>

</body>
</html>
```